Business Card Ayurvedic Massage

I'm starting with my ayurvedic massage business and need a business card design. The design should be inline with my brand/logo as well as with the design of my website (www.mirelo-dant.ch).
Front: logo and text "Ayurvedische Massagen"
back: name and adress (see details https://www.mirelo-dant.ch/kontakt.html)

```html
<!DOCTYPE html>
<html lang="de">
<head>
<meta charset="utf-8">
<title>Mirelo-Dant – Visitenkarte</title>
<link rel="stylesheet" href="https://fonts.googleapis.com/css2?family=Amita:wght@700&family=Crimson+Text:wght@400;600&display=swap">
<style>
  :root {
    --stage: #ece7df;
    --red-light: #c0171f;
    --red-mid: #a01118;
    --red-deep: #6e0a0e;
    --gold: #e0b646;
    --gold-dark: #b88a22;
    --band-tint: #b5161e;
  }
  * { box-sizing: border-box; margin: 0; padding: 0; }
  html, body { width: 1200px; height: 780px; overflow: hidden; }
  body {
    background: var(--stage);
    position: relative;
    font-family: "Crimson Text", Georgia, serif;
  }
  .card {
    position: absolute;
    border-radius: 22px;
    overflow: hidden;
    box-shadow: 0 10px 28px rgba(0,0,0,0.22);
  }
  /* Contact side */
  .card-contact {
    left: 70px; top: 220px; width: 560px; height: 340px;
    background: radial-gradient(ellipse at 55% 35%, var(--red-light) 0%, var(--red-mid) 55%, var(--red-deep) 100%);
    display: flex; align-items: center; justify-content: center;
  }
  .contact-block { text-align: center; color: var(--gold); }
  .contact-name {
    font-family: "Amita", "Crimson Text", serif;
    font-weight: 700;
    font-size: 40px;
    line-height: 1.1;
    margin-bottom: 6px;
  }
  .contact-role { font-size: 17px; margin-bottom: 14px; }
  .contact-line { font-size: 16px; line-height: 1.45; }
  .contact-line .icon { display: inline-block; vertical-align: -1px; margin: 0 5px 0 0; }
  .contact-line .sep { margin: 0 8px; }
  .contact-web {
    font-size: 16px; font-weight: 600; letter-spacing: 1px; margin-top: 10px;
  }
  /* Logo side */
  .card-logo {
    left: 760px; top: 110px; width: 340px; height: 560px;
    background: linear-gradient(90deg, var(--red-deep) 0%, var(--red-mid) 30%, var(--red-mid) 70%, var(--red-deep) 100%);
  }
  .logo-band {
    position: absolute; left: 95px; top: 0; width: 150px; height: 100%;
    background: radial-gradient(ellipse at 50% 50%, var(--band-tint) 0%, var(--red-mid) 100%);
    border-left: 3px solid var(--gold);
    border-right: 3px solid var(--gold);
  }
  .logo-band::before, .logo-band::after {
    content: ""; position: absolute; top: 0; height: 100%; width: 1px; background: var(--gold-dark);
  }
  .logo-band::before { left: -12px; }
  .logo-band::after { right: -12px; }
  .brand-name {
    position: absolute; left: 50%; top: 50%;
    transform: translate(-50%, -50%) rotate(90deg);
    white-space: nowrap;
    font-size: 34px; font-weight: 600; color: var(--gold);
    letter-spacing: 1px;
  }
</style>
</head>
<body>
  <section class="card card-contact">
    <div class="contact-block">
      <p class="contact-name">Lena Varos</p>
      <p class="contact-role">Ayurveda Massage Praktikerin</p>
      <p class="contact-line">Lindenweg 14</p>
      <p class="contact-line">CH - 8700 Talwil (ZH)</p>
      <p class="contact-line">
        <svg class="icon" width="11" height="13" viewBox="0 0 11 13" aria-hidden="true"><rect x="1" y="1" width="9" height="11" rx="1.5" fill="none" stroke="currentColor" stroke-width="1.4"/></svg>+41 77 000 12 34<span class="sep">|</span><svg class="icon" width="12" height="10" viewBox="0 0 12 10" aria-hidden="true"><rect x="0.5" y="0.5" width="11" height="9" fill="currentColor"/><path d="M1 1l5 4.5L11 1" fill="none" stroke="#a01118" stroke-width="1.2"/></svg>info@mirelo-dant.ch
      </p>
      <p class="contact-web">www.mirelo-dant.ch</p>
    </div>
  </section>

  <section class="card card-logo">
    <div class="logo-band">
      <p class="brand-name">Mirelo-Dant</p>
    </div>
  </section>
</body>
</html>
```